new signage design for budget motel - Brookfern Lodge

renaming the budget motel as Brookfern Lodge, property located on side of a hill. therefore i choose to name is Brookfern Lodge, im looking for clean, modern look in signage design,this property does not have a Logo, plan to us signage design as a logo as well. current pole sign housing is rectangle shape and will be using same housing I'll be attaching picture of the signage for better idea. looking forward to awesome creative designs.

Industry/Entity Type

Motel

Font styles to use
Serif
Sans Serif

Requirements
Should not have
• mountains , mountain(s) with snow , trees, no black color, red color, blue letters, too much green.

```html
<!DOCTYPE html>
<html lang="en">
<head>
<meta charset="UTF-8">
<title>Brookfern Lodge – Pole Sign</title>
<link rel="stylesheet" href="https://fonts.googleapis.com/css2?family=Cormorant+Garamond:wght@600&display=swap">
<style>
  :root {
    --page-bg: #f2f2f2;
    --sign-brown: #3b1a0b;
    --sign-gold: #ffc20e;
    --sign-edge: #ffffff;
    --lettering: #3b1a0b;
  }
  html, body {
    margin: 0;
    padding: 0;
    width: 800px;
    height: 1200px;
    overflow: hidden;
    background: var(--page-bg);
  }
  .canvas {
    width: 800px;
    height: 1200px;
    display: flex;
    align-items: center;
    justify-content: center;
  }
  .sign-face {
    width: 720px;
    height: 514px;
    display: block;
    box-shadow: 0 2px 6px rgba(0,0,0,0.18);
  }
  .sign-face .frame { fill: var(--sign-brown); }
  .sign-face .panel {
    fill: var(--sign-gold);
    stroke: var(--sign-edge);
    stroke-width: 3;
  }
  .sign-face .brand-line {
    font-family: "Cormorant Garamond", Georgia, serif;
    font-style: normal;
    font-weight: 600;
    font-size: 104px;
    letter-spacing: 2px;
    fill: var(--lettering);
  }
</style>
</head>
<body>
  <main class="canvas">
    <svg class="sign-face" viewBox="0 0 720 514" xmlns="http://www.w3.org/2000/svg" role="img" aria-label="Brookfern Lodge sign">
      <rect class="frame" x="0" y="0" width="720" height="514"/>
      <polygon class="panel" points="144,0 576,0 720,164 720,350 576,514 144,514 0,350 0,164"/>
      <text class="brand-line" x="360" y="238" text-anchor="middle">Brookfern</text>
      <text class="brand-line" x="360" y="346" text-anchor="middle">Lodge</text>
    </svg>
  </main>
</body>
</html>
```